Webdesign für Birke Werkstatt
Zielgruppe
Birke Werkstatt produziert GfK Formteile und Abdeckungen
Einzelanfertigungen • Negativ - Formenbau • Prototyping • Ur-Modellbau
Formteile • Abdeckungen • Behälter • Sonderanfertigungen • Beschichtungen
Prototypen Modellbau • Anfertigung von Negativformen • Reparaturen • Fahrzeugteile
Hauptzielgruppe ist die Luftfahrtindustrie (Abdeckungen für Triebwerke)
Durch den Prototypenbau und die Einzelanfertigungen ist die Zielgruppe nicht klar zu definieren. Es werden Einzelteile jeglicher Art aus GfK hergestellt.
Dies können auch Anbauteile für PKW, Poolbeschichtungen, Teile für Boote etc sein.
Es gibt auch Kleinserien. Beispielsweise baut Birke-Werkstatt Motorhauben für Hallo-Brenner Rasenmähertrecker aus den 70er Jahren nach, die es nicht mehr zu kaufen gibt.
Aufgabenstellung
Der Designer hat alle Freiheiten. Die Seite muss natürlich responsiv funktionieren.
Außer dem Logo gibt es keine must-haves.
Schriftart aus dem Logo: EXO 2

```html
<!DOCTYPE html>
<html lang="de">
<head>
<meta charset="utf-8">
<title>Birke Werkstatt – GfK Formteile</title>
<link href="https://fonts.googleapis.com/css2?family=Exo+2:ital,wght@0,300;0,400;0,500;0,700;0,800;1,600&display=swap" rel="stylesheet">
<style>
:root{
  --blue:#175f9e;
  --blue-dark:#124f86;
  --blue-deep:#0f3f6e;
  --text:#333;
  --grey-bg:#f0f0f0;
  --tile:#efefef;
  --orange:#f5a100;
  --white:#fff;
}
*{box-sizing:border-box;margin:0;padding:0}
html,body{width:1200px;height:2729px;overflow:hidden}
body{position:relative;font-family:"Exo 2",sans-serif;color:var(--text);background:var(--white)}
.abs{position:absolute}

/* header */
.brand{left:108px;top:58px;display:flex;align-items:center;gap:18px}
.brand-dot{width:150px;height:150px;border-radius:50%;background:var(--blue)}
.brand-name{font-size:62px;font-weight:800;color:var(--blue);line-height:1}
.brand-tag{font-size:20px;color:#555;margin-top:10px}
.meta{top:18px;right:110px;display:flex;gap:24px;align-items:center;font-size:15px;color:var(--blue)}
.flag{width:36px;height:22px;display:flex;flex-direction:column;box-shadow:0 1px 3px rgba(0,0,0,.3)}
.flag span{flex:1}

.nav{left:0;top:180px;width:1200px;height:51px;background:var(--blue);display:flex;padding-left:303px}
.nav a{color:var(--white);text-decoration:none;font-size:17px;line-height:51px;padding:0 22px;position:relative}
.nav a.active{background:var(--blue-dark)}
.nav a.active::after{content:"";position:absolute;left:50%;bottom:-8px;margin-left:-8px;border:8px solid transparent;border-top-color:var(--blue-dark);border-bottom:0}

/* hero */
.hero{left:0;top:231px;width:1200px;height:491px;background:linear-gradient(180deg,#9eb6c9 0%,#d9e2ea 45%,#b9bfc4 70%,#8d8e8a 100%)}
.hero-caption{left:808px;top:266px;width:392px;height:111px;background:rgba(255,255,255,.9);padding:20px 0 0 33px;font-size:31px;font-weight:800;color:var(--blue);line-height:36px}
.arrow{width:62px;height:62px;background:rgba(255,255,255,.85);display:flex;align-items:center;justify-content:center}

/* about */
.h2{width:1200px;left:0;text-align:center;font-size:31px;font-weight:800;color:var(--blue)}
.about-img{left:108px;top:837px;width:453px;height:333px;background:linear-gradient(135deg,#2f6fc4,#5b93d8 55%,#cfd6dc)}
.about-text{left:108px;top:1193px;width:460px;font-size:17px;line-height:26.6px;font-weight:300;color:#222}
.feature{left:641px;width:448px;height:60px;background:var(--tile);display:flex;align-items:center;padding-left:20px;gap:20px;font-size:21px;color:var(--blue)}

/* products */
.products{left:0;top:1441px;width:1200px;height:820px;background:var(--grey-bg)}
.view-icons{left:1005px;top:1510px;display:flex;gap:10px}
.card{top:1590px;width:289px;height:503px;background:var(--white);box-shadow:0 2px 6px rgba(0,0,0,.08);text-align:center}
.card-img{margin:13px;height:262px}
.card h3{font-size:19px;font-weight:800;color:var(--blue);line-height:24px;height:58px;padding:0 10px}
.card p{font-size:17px;line-height:21px;color:#333;height:80px;padding:0 18px;display:flex;align-items:center;justify-content:center}
.btn{display:inline-block;margin-top:8px;width:102px;height:31px;line-height:31px;background:var(--orange);color:var(--white);font-weight:700;font-size:16px;box-shadow:0 6px 8px -4px rgba(245,161,0,.6)}

/* contact */
.contact-tab{left:90px;top:2217px;width:203px;height:46px;background:var(--blue);clip-path:polygon(18px 0,100% 0,100% 100%,0 100%);color:var(--white);font-size:30px;font-weight:800;padding-left:48px;line-height:48px}
.footer{left:0;top:2261px;width:1200px;height:468px;background:var(--blue);color:var(--white)}
.f-name{left:137px;top:2295px;font-size:30px;font-weight:800}
.f-addr{left:137px;top:2348px;font-size:20px;line-height:24px}
.f-tel{left:137px;top:2444px;font-size:20px;line-height:24px}
.f-tel span{display:inline-block;width:60px}
.f-head{left:661px;top:2298px;font-size:26px;font-weight:700}
.field{left:641px;width:447px;background:var(--white);border:1px solid #c9d6e3;color:var(--blue);font-size:20px;padding:7px 20px}
.send{left:969px;top:2627px;width:121px;height:39px;background:var(--blue-deep);color:var(--white);font-weight:800;font-size:18px;line-height:39px;text-align:center;letter-spacing:.5px}
</style>
</head>
<body>

<header>
  <div class="abs brand">
    <div class="brand-dot"></div>
    <div>
      <div class="brand-name">Birke Werkstatt</div>
      <div class="brand-tag">GfK Formteile | Ur-Modellbau | Prototyping</div>
    </div>
  </div>
  <div class="abs meta">
    <span>Impressum</span><span>AGB</span>
    <div class="flag"><span style="background:#000"></span><span style="background:#dd0000"></span><span style="background:#ffce00"></span></div>
  </div>
  <nav class="abs nav">
    <a class="active">Startseite</a><a>Über uns</a><a>Produkte &amp; Dienstleistungen</a><a>Kontakt</a>
  </nav>
</header>

<section>
  <div class="abs hero" role="img" aria-label="Passagierflugzeug auf dem Vorfeld mit Schlepper unter bewölktem Himmel"></div>
  <div class="abs hero-caption">Abdeckungen für<br>Triebwerke</div>
  <div class="abs arrow" style="left:0;top:452px"><svg width="22" height="30" viewBox="0 0 22 30"><path d="M17 3 5 15l12 12" fill="none" stroke="#175f9e" stroke-width="5"/></svg></div>
  <div class="abs arrow" style="left:1138px;top:452px"><svg width="22" height="30" viewBox="0 0 22 30"><path d="M5 3l12 12L5 27" fill="none" stroke="#175f9e" stroke-width="5"/></svg></div>
</section>

<section>
  <h2 class="abs h2" style="top:757px">Über uns</h2>
  <div class="abs about-img" role="img" aria-label="Triebwerk unter blauer Schutzabdeckung auf Transportgestell"></div>
  <p class="abs about-text">Wir entwickeln und fertigen geometrisch anspruchsvolle Formteile von höchster Qualität. Die von uns konzipierten Verbundwerkstoffe mit ihren herausragenden Ober-flächen- und Materialeigenschaften bieten konstruktive Vorteile und erweitern die gestalterischen Möglichkeiten.</p>
  <div class="abs feature" style="top:839px">
    <svg width="40" height="28" viewBox="0 0 40 28"><path d="M2 8l10-5 8 4 8-4 10 5-6 10-10 8-6-4-8-5z" fill="#175f9e"/></svg>Kundenorientiert</div>
  <div class="abs feature" style="top:918px">
    <svg width="40" height="28" viewBox="0 0 40 28"><path d="M4 26a16 16 0 0 1 32 0" fill="none" stroke="#175f9e" stroke-width="5"/><path d="M20 24l8-10" stroke="#175f9e" stroke-width="4"/></svg>Leistungsstark</div>
</section>

<section>
  <div class="abs products"></div>
  <h2 class="abs h2" style="top:1501px">Produkte &amp; Dienstleistungen</h2>
  <div class="abs view-icons">
    <svg width="44" height="24" viewBox="0 0 44 24"><path d="M8 4 2 12l6 8M36 4l6 8-6 8" fill="none" stroke="#175f9e" stroke-width="3"/><rect x="14" y="2" width="12" height="20" fill="#175f9e"/><rect x="26" y="4" width="4" height="16" fill="#175f9e"/></svg>
    <svg width="28" height="24" viewBox="0 0 28 24" fill="#666"><rect x="0" y="0" width="8" height="7"/><rect x="10" y="0" width="8" height="7"/><rect x="20" y="0" width="8" height="7"/><rect x="0" y="9" width="8" height="6"/><rect x="10" y="9" width="8" height="6"/><rect x="20" y="9" width="8" height="6"/><rect x="0" y="17" width="8" height="7"/><rect x="10" y="17" width="8" height="7"/><rect x="20" y="17" width="8" height="7"/></svg>
  </div>
  <div class="abs arrow" style="left:21px;top:1741px;background:#fff"><svg width="22" height="30" viewBox="0 0 22 30"><path d="M17 3 5 15l12 12" fill="none" stroke="#175f9e" stroke-width="5"/></svg></div>
  <div class="abs arrow" style="left:1113px;top:1741px;background:#fff"><svg width="22" height="30" viewBox="0 0 22 30"><path d="M5 3l12 12L5 27" fill="none" stroke="#175f9e" stroke-width="5"/></svg></div>

  <article class="abs card" style="left:108px">
    <div class="card-img" role="img" aria-label="Gelber Triebwerksdeckel aus GfK" style="background:linear-gradient(135deg,#d6e63a,#b9c92a 60%,#9aa3a8)"></div>
    <h3>Luftfahrt Formbauteile</h3>
    <p>Anfertigung von Triebwerkcover für jeden Triebwerktypen.</p>
    <span class="btn">Details</span>
  </article>
  <article class="abs card" style="left:455px">
    <div class="card-img" role="img" aria-label="Aufblasbare graue Sonderabdeckung in einer Halle" style="background:linear-gradient(135deg,#c9cfd4,#9ea7ae 60%,#6c747a)"></div>
    <h3>Aufblasbare Sonderabdeckungen</h3>
    <p>Anfertigung von Triebwerkcover für jeden Triebwerktypen.</p>
    <span class="btn">Details</span>
  </article>
  <article class="abs card" style="left:801px">
    <div class="card-img" role="img" aria-label="Blaue technische Formbauteile in Ringform" style="background:linear-gradient(135deg,#2a5fd0,#1f4fb8 60%,#c8b860)"></div>
    <h3>Formbauteile</h3>
    <p>Anfertigung von technischen Formbauteilen (Einzelstück oder Kleinserien).</p>
    <span class="btn">Details</span>
  </article>
</section>

<footer>
  <div class="abs contact-tab">Kontakt</div>
  <div class="abs footer"></div>
  <div class="abs f-name" style="color:#fff">Birke Werkstatt</div>
  <div class="abs f-addr" style="color:#fff">Geschäftsführer: M. Falkner<br>Lindenhofweg 14<br>30986 Ostervalde</div>
  <div class="abs f-tel" style="color:#fff"><span>Tel.</span>+49 555 / 012 34 56<br><span>Fax.</span>+49 555 / 012 34 57</div>
  <div class="abs f-head" style="color:#fff">Ihre Nachricht</div>
  <div class="abs field" style="top:2345px;height:43px">Name</div>
  <div class="abs field" style="top:2406px;height:43px">E-Mail</div>
  <div class="abs field" style="top:2467px;height:145px;padding-top:10px">Nachricht</div>
  <div class="abs send">SENDEN</div>
</footer>

</body>
</html>
```